verdant harbour requires some business cards

I need some business cards created that feature the company's newly designed logo. The business cards need to be be double sided and be a standard Australian size of 90mm x 55mm

Target Market(s)

business professionals, company executives, local goverment

Industry/Entity Type

Business

Requirements
Must have
• Company's logo
• The information section must include
• Individual name:
• Position:
• Phone:
• Address:
• Email:
• Website: www.verdantharbour.example
• The cards need to be easily formatted so I can enter staff members details positions etc...
• I plan to get these printed at deskmarket so can you please ensure that all designs meet their printing requirements http://www.deskmarket.example/retail/b2c/opsProductCreate.do?qty=1&cardQty=1000&sided=double&productname=colourbusinesscards&category=businesscards
Nice to have
• I might like to see some of the services we offer printed on one of the faces:
• Lighting Design (architectural, commercial, residential, theatrical ,exterior, interior) Lighting Consultancy, Theatrical Consultancy

```html
<!DOCTYPE html>
<html lang="en">
<head>
<meta charset="utf-8">
<title>verdant harbour – business cards</title>
<link rel="stylesheet" href="https://fonts.googleapis.com/css2?family=Montserrat:wght@400;600;700&display=swap">
<style>
  :root {
    --page: #ffffff;
    --card-edge: #ececec;
    --brand-blue: #3790d0;
    --brand-blue-light: #5aa6dc;
    --ink-dark: #3a3a3c;
    --ink-muted: #9a9a9a;
    --ink-light: #ffffff;
    --ink-light-soft: rgba(255, 255, 255, 0.85);
  }
  html, body {
    margin: 0;
    padding: 0;
    width: 1200px;
    height: 754px;
    overflow: hidden;
    background: var(--page);
    font-family: "Montserrat", Arial, sans-serif;
  }
  .sheet {
    position: relative;
    width: 1200px;
    height: 754px;
  }
  .card {
    position: absolute;
    top: 210px;
    width: 508px;
    height: 311px;
    box-sizing: border-box;
    overflow: hidden;
  }
  .card--front {
    left: 1px;
    background: var(--page);
    border: 1px solid var(--card-edge);
  }
  .card--back {
    left: 581px;
    background: var(--brand-blue);
    color: var(--ink-light);
  }
  .card__texture {
    position: absolute;
    inset: 0;
    background:
      radial-gradient(ellipse 150px 110px at 420px 40px, rgba(255,255,255,0.10), rgba(255,255,255,0) 70%),
      radial-gradient(ellipse 120px 160px at 470px 240px, rgba(255,255,255,0.09), rgba(255,255,255,0) 70%),
      radial-gradient(ellipse 200px 90px at 160px 80px, rgba(255,255,255,0.06), rgba(255,255,255,0) 70%);
  }
  .brand {
    position: absolute;
    left: 78px;
    top: 126px;
  }
  .brand__name {
    margin: 0;
    font-size: 44px;
    font-weight: 400;
    letter-spacing: -0.5px;
    line-height: 1;
    color: var(--ink-dark);
  }
  .brand__tagline {
    margin: 10px 0 0 14px;
    font-size: 7.5px;
    letter-spacing: 3.2px;
    color: var(--ink-muted);
  }
  .contact {
    position: absolute;
    left: 36px;
    top: 128px;
  }
  .contact__name {
    margin: 0;
    font-size: 21px;
    font-weight: 700;
    line-height: 1;
  }
  .contact__position {
    margin: 6px 0 0;
    font-size: 11.5px;
    font-weight: 400;
    color: var(--ink-light-soft);
  }
  .contact__phone {
    margin: 10px 0 0;
    font-size: 12.5px;
    font-weight: 700;
  }
  .contact__lines {
    margin: 9px 0 0;
    font-size: 12.5px;
    line-height: 15px;
    font-weight: 400;
  }
  .contact__address {
    margin-top: 14px;
  }
</style>
</head>
<body>
  <main class="sheet">
    <section class="card card--front" aria-label="Card front">
      <div class="brand">
        <p class="brand__name">verdant harbour</p>
        <p class="brand__tagline">Lighting Design &amp; Consultancy</p>
      </div>
    </section>

    <section class="card card--back" aria-label="Card back">
      <div class="card__texture" role="img" aria-label="Faint light-blue decorative pattern across the card back"></div>
      <div class="contact">
        <p class="contact__name">Daniel Whitcombe</p>
        <p class="contact__position">Senior Lighting Designer</p>
        <p class="contact__phone">+61 8 9000 4127</p>
        <p class="contact__lines">daniel@verdantharbour.example<br>www.verdantharbour.example</p>
        <p class="contact__lines contact__address">PO Box 482, Perth<br>WA 6000 Australia</p>
      </div>
    </section>
  </main>
</body>
</html>
```